Dentist Seminar invite please see .doc in attachments

Need an 8.5 x 11 invite designed. It will be for an invitation to attend an evening seminar on dental procedures. Feel free to utilize both front and back ONLY IF REQUIRED

See Assets & PPT with additional assets.

INSPIRATION: FIle NAME BRELOW

Target Market(s)

Dentists

Industry/Entity Type

Dental

Font styles to use
Other font styles liked:
• lato, garamond, palatino linotype

Colors
cee9f5
9bcb3c
0492cd
cadf82

Requirements
Must have
• Must have the colours suggested, and professional feel.
• Some of the assets merged cleanly into the design
Should not have
• Any pictures of teeth, tooth brushes or any dental product

```html
<!DOCTYPE html>
<html lang="en">
<head>
<meta charset="utf-8">
<title>Digital Dentistry Evening Seminar – Invitation</title>
<link rel="stylesheet" href="https://fonts.googleapis.com/css2?family=Lato:wght@400;700;900&family=EB+Garamond:wght@400;500&display=swap">
<style>
  :root{
    --blue:#0492cd;
    --blue-deep:#0a6fc0;
    --sky:#cee9f5;
    --green:#9bcb3c;
    --lime:#cadf82;
    --charcoal:#3d3d3f;
    --ink:#1b1b1f;
    --navy:#0d1a33;
    --stage:#4a4a4a;
    --paper:#ffffff;
  }
  *{box-sizing:border-box;margin:0;padding:0}
  html,body{width:1200px;height:1200px;overflow:hidden}
  body{background:var(--stage);font-family:'Lato',sans-serif;position:relative}
  .page{position:absolute;top:272px;width:510px;height:656px;background:var(--paper);overflow:hidden}
  .page--front{left:58px}
  .page--back{left:632px}
  .page svg.shapes{position:absolute;inset:0;width:510px;height:656px}
  .abs{position:absolute}

  .brand{font-family:'Lato',sans-serif;font-weight:900;color:var(--ink);font-size:19px;letter-spacing:-.3px;line-height:1}
  .rule{height:1.5px;background:var(--blue);width:75px}

  /* front */
  .front-brand{right:30px;top:234px;text-align:right}
  .tagline{right:30px;top:262px;text-align:right;line-height:1.2}
  .tagline__lead{font-family:'EB Garamond',serif;color:var(--blue);font-size:20px}
  .tagline__main{font-weight:700;color:var(--ink);font-size:14.5px;letter-spacing:.2px}
  .tagline-rule{right:30px;top:334px}
  .synopsis{right:32px;top:362px;width:202px}
  .section-title{color:var(--blue);font-weight:700;font-size:11.5px;text-align:right;margin-bottom:10px}
  .synopsis p{font-size:7.1px;line-height:1.37;text-align:justify;color:var(--ink);text-align-last:right}
  .web-rule{right:32px;top:574px}
  .web{right:32px;top:584px;font-family:'EB Garamond',serif;font-size:15.5px;color:var(--ink);letter-spacing:.4px}

  .objectives{left:34px;top:320px;width:180px}
  .objectives__title{font-size:11.5px;line-height:1.3;color:#fff}
  .objectives__title span{color:var(--blue);display:block}
  .objectives .rule{width:42px;margin:4px 0 16px;background:var(--blue)}
  .objectives ul{list-style:none}
  .objectives li{position:relative;font-size:7.3px;line-height:1.3;color:#fff;padding-left:12px;margin-bottom:5.5px;text-align:justify}
  .objectives li::before{content:"";position:absolute;left:0;top:2px;width:5px;height:5px;border-radius:50%;border:1px solid var(--blue)}

  /* back */
  .event{right:36px;top:36px;text-align:right;color:var(--navy);font-weight:700}
  .event__date{color:#fff;font-size:23px;line-height:1.05;letter-spacing:-.2px}
  .event__time{font-size:23px;line-height:1.2;margin-bottom:10px}
  .event__venue{color:#fff;font-size:16px;line-height:1.2}
  .event__line{font-size:15.5px;line-height:1.25}
  .event__label{color:#fff;font-size:16px;margin-top:10px;line-height:1.2}
  .back-brand{left:26px;top:438px}
  .back-rule{left:28px;top:466px}
  .bio{left:28px;top:480px;width:176px}
  .bio h2{font-size:12px;font-weight:400;color:var(--ink);margin-bottom:6px;letter-spacing:.2px}
  .bio p{font-size:7.2px;line-height:1.33;text-align:justify;color:#333}
</style>
</head>
<body>

<!-- FRONT -->
<section class="page page--front">
  <svg class="shapes" viewBox="0 0 510 656" aria-hidden="false">
    <defs>
      <linearGradient id="blueSweep" x1="0" y1="0" x2="1" y2="1">
        <stop offset="0" stop-color="#0a6fc0"/>
        <stop offset=".55" stop-color="#0492cd"/>
        <stop offset="1" stop-color="#14a6e0"/>
      </linearGradient>
      <linearGradient id="warmPhoto" x1="0" y1="0" x2="1" y2="1">
        <stop offset="0" stop-color="#efe4d6"/>
        <stop offset=".5" stop-color="#b98763"/>
        <stop offset="1" stop-color="#5a3a2c"/>
      </linearGradient>
    </defs>
    <polygon points="380,0 510,0 510,165 318,212" fill="url(#blueSweep)"/>
    <polygon points="0,180 95,238 0,282" fill="url(#blueSweep)"/>
    <polygon points="0,282 322,194 197,638 0,638" fill="var(--charcoal)"/>
    <path d="M0,0 H405 Q428,0 432,18 Q436,40 420,58 L218,322 Q205,338 190,326 L0,192 Z" fill="url(#warmPhoto)" role="img" aria-label="Photo of a smiling young couple"/>
    <path d="M0,192 L190,326 Q205,338 218,322 L352,144" fill="none" stroke="var(--green)" stroke-width="3"/>
    <rect x="0" y="638" width="510" height="18" fill="var(--green)"/>
  </svg>

  <div class="abs brand front-brand">Veranta Group</div>
  <div class="abs tagline">
    <div class="tagline__lead">United for</div>
    <div class="tagline__main">GLOBAL EXCELLENCE<br>IN DENTISTRY</div>
  </div>
  <div class="abs rule tagline-rule"></div>

  <div class="abs synopsis">
    <div class="section-title">SYNOPSIS:</div>
    <p>This presentation will cover the recent advances in digital technology and its use in dentistry. Digital protocols will be introduced that can improve upon traditional treatment planning approaches. The use of modern 3D technology and the digital workflow can simplify advanced procedures enhancing the predictability of the surgical outcomes. Through the use of state of the art diagnostic imaging technologies, intra-oral scanning, live guided navigation, and 3D printing; multiple digital workflows and their surgical applications will be discussed through real clinical cases from Dr Brelow's surgical practice. This groundbreaking lecture will showcase the synergy between advanced technology and fundamental biological principles to revolutionize the modern practice of periodontics and implantology. Multiple innovative protocols to treat advanced surgical cases will be presented with techniques that have never been seen before.</p>
  </div>
  <div class="abs rule web-rule"></div>
  <div class="abs web">www.verantagroup.com</div>

  <div class="abs objectives">
    <div class="objectives__title"><span>LEARNING</span>OBJECTIVES:</div>
    <div class="rule"></div>
    <ul>
      <li>Discuss the use of modern digital technologies like CBCT, intra-oral scanning, and 3D printing.</li>
      <li>Learn to digitally plan surgical procedures and use 3D printed surgical guides</li>
      <li>Understand the benefits of microsurgery and the use of surgical operating microscope</li>
      <li>Understand the benefits of digital technology in surgical treatment planning</li>
      <li>Understanding and benefits of live guided navigation surgery and its applications</li>
      <li>Learn about innovative procedures like digitally guided bone block harvesting, digitally created bone grafts, and osteotomy guides.</li>
      <li>Understand how computer automated design software can improve upon real live surgery.</li>
    </ul>
  </div>
</section>

<!-- BACK -->
<section class="page page--back">
  <svg class="shapes" viewBox="0 0 510 656">
    <defs>
      <linearGradient id="blueSweep2" x1="0" y1="0" x2="1" y2="1">
        <stop offset="0" stop-color="#0a6fc0"/>
        <stop offset=".5" stop-color="#0492cd"/>
        <stop offset="1" stop-color="#1aa8e2"/>
      </linearGradient>
      <linearGradient id="coatTones" x1="0" y1="0" x2="0" y2="1">
        <stop offset="0" stop-color="#f2f2f2"/>
        <stop offset=".55" stop-color="#dfe6ee"/>
        <stop offset="1" stop-color="#cdbb9c"/>
      </linearGradient>
      <linearGradient id="scanTones" x1="0" y1="0" x2="1" y2="1">
        <stop offset="0" stop-color="#e4e1da"/>
        <stop offset="1" stop-color="#b9b4aa"/>
      </linearGradient>
    </defs>
    <polygon points="164,0 510,0 510,240 326,318" fill="url(#blueSweep2)"/>
    <polygon points="326,318 510,240 510,638 210,638" fill="var(--charcoal)"/>
    <rect x="325" y="240" width="175" height="398" rx="40" fill="url(#coatTones)" role="img" aria-label="Photo of a smiling dentist in a white coat holding a clipboard"/>
    <rect x="34" y="30" width="130" height="105" rx="14" fill="url(#scanTones)" role="img" aria-label="3D scan of a jaw with implant planning"/>
    <rect x="34" y="170" width="125" height="100" rx="14" fill="url(#scanTones)" role="img" aria-label="3D model of a surgical guide on an arch"/>
    <rect x="34" y="300" width="118" height="88" rx="14" fill="url(#scanTones)" role="img" aria-label="3D render of an arch with implants"/>
    <rect x="180" y="304" width="122" height="78" rx="14" fill="url(#scanTones)" role="img" aria-label="3D render of an upper jaw bone"/>
    <rect x="0" y="638" width="510" height="18" fill="var(--green)"/>
  </svg>

  <div class="abs event">
    <div class="event__date">NOVEMBER 13</div>
    <div class="event__time">2017/ 6:30 – 9:30PM</div>
    <div class="event__venue">MAPLE HALL EVENT CENTRE</div>
    <div class="event__line">480 Harbourline Ave. Toronto,</div>
    <div class="event__line">Ontario M4X 1B7</div>
    <div class="event__label">REGISTRATION:</div>
    <div class="event__line">events@verantagroup.com</div>
    <div class="event__line">416-555-0142</div>
  </div>

  <div class="abs brand back-brand">Veranta Group</div>
  <div class="abs rule back-rule"></div>
  <div class="abs bio">
    <h2>BIOGRAPHY</h2>
    <p>Lorem Ipsum is simply dummy text of the printing and typesetting industry. Lorem Ipsum has been the industry's standard dummy text ever since the 1500s, when an unknown printer took a galley of type and scrambled it to make a type specimen book. It has survived not only five centuries, but also the leap into electronic typesetting, remaining essentially unchanged. It was popularised in the 1960s with the release of Letraset sheets containing Lorem Ipsum passages, and more recently with desktop publishing software like Aldus PageMaker including versions of</p>
  </div>
</section>

</body>
</html>
```